Business card design for modern LaneScope agency

Hello,

I need a business card design for my company Harbor9Studio.
We mainly offer Vornix LaneScope Tours (360° Photography) and it should be a business card with following details:

Name: Tobias Merland
Number: +49 160 55 82 907
Mail: tobias@harbor9studio.example
website: harbor9studio.example

Main colour that we use is the red of the logo.
It´s also important to integrate the "Vornix Gold logo" as the person on this business card is a Vornix Gold photographer.

And if possible we would also like to integrate something like send us a sms or pingwell and we call you back. As the number is german but we sell now in Vienna, Austria.

We offer a good price but very high photography quality, as we are mostly students - that´s our concept.

Maybe an idea is to integrate something 360° on the back-side of the card, for example the photo attached (just an idea) or some great design.
See flyer (attached) and harbor9studio.example for inspiration, maybe use of the photo of me (attached) in a circle or something

I´m very excited for your designs and thanks a lot in advance!! :)

Target Market(s)

Shops, hotels, shopping centers, etc. in Vienna, Austria

Industry/Entity Type

Business

Contact Information for Business Card

double-sided, use red of the logo, 360° vornix lanescope certified photographer

Font styles to use
Serif
Sans Serif

Colors
ec1f27

Requirements
Nice to have
• maybe some 360° design on back-side
• maybe include photo of me in a circle or something or sketched in red colour

```html
<!DOCTYPE html>
<html lang="en">
<head>
<meta charset="utf-8">
<title>Harbor9Studio – Business Card</title>
<link rel="stylesheet" href="https://fonts.googleapis.com/css2?family=Oswald:wght@400;500&family=Open+Sans:ital,wght@0,400;1,400&display=swap">
<style>
  :root {
    --brand-red: #e2192f;
    --band-red: #e31b34;
    --logo-grey: #a3a4a8;
    --ink: #3b3b3b;
    --divider: #8a8a8a;
    --paper: #ffffff;
    --stage: #1f1f1f;
    --photo-warm: #c9a47e;
    --photo-wall: #7d1f24;
    --photo-floor: #5e4434;
  }
  html, body {
    margin: 0;
    width: 1200px;
    height: 987px;
    overflow: hidden;
    background: var(--stage);
  }
  .canvas {
    position: relative;
    width: 1200px;
    height: 987px;
  }
  .card {
    position: absolute;
    left: 293px;
    width: 615px;
    height: 352px;
    overflow: hidden;
    box-shadow: 0 4px 14px rgba(0,0,0,.45);
  }
  .card--front { top: 130px; background: var(--paper); }
  .card--back  { top: 505px; }

  /* brand lockup */
  .brand {
    position: absolute;
    display: flex;
    align-items: center;
    gap: 10px;
    font-family: "Oswald", sans-serif;
    font-weight: 500;
    line-height: .95;
    text-transform: uppercase;
  }
  .brand__square {
    background: var(--brand-red);
    flex: none;
  }
  .brand--front { left: 45px; top: 135px; }
  .brand--front .brand__square { width: 58px; height: 67px; }
  .brand--front .brand__name { font-size: 33px; color: var(--logo-grey); }
  .brand--back { left: 427px; top: 22px; gap: 7px; }
  .brand--back .brand__square { width: 40px; height: 46px; }
  .brand--back .brand__name { font-size: 23px; color: var(--ink); }

  .divider {
    position: absolute;
    left: 321px; top: 46px;
    width: 1px; height: 249px;
    background: var(--divider);
  }
  .portrait {
    position: absolute;
    left: 354px; top: 42px;
    width: 130px; height: 130px;
    border-radius: 50%;
    border: 2px solid var(--brand-red);
    background: radial-gradient(circle at 50% 40%, #8a8a8a, #3c3c3c 75%);
  }
  .person {
    position: absolute;
    left: 354px; top: 190px;
    margin: 0;
    font-family: "Oswald", sans-serif;
    font-weight: 500;
    font-size: 24px;
    color: var(--brand-red);
    text-transform: uppercase;
    letter-spacing: .3px;
  }
  .contact {
    position: absolute;
    left: 354px; top: 232px;
    margin: 0; padding: 0;
    list-style: none;
    font-family: "Open Sans", sans-serif;
    font-size: 14.5px;
    color: var(--ink);
  }
  .contact li {
    display: flex;
    align-items: center;
    gap: 8px;
    height: 23.5px;
  }
  .contact svg { width: 14px; height: 14px; fill: var(--brand-red); flex: none; }
  .rule-grey {
    position: absolute; left: 0; right: 0; top: 334px;
    height: 2px; background: #c9c9c9;
  }
  .rule-red {
    position: absolute; left: 0; right: 0; top: 340px;
    height: 12px; background: var(--band-red);
  }

  /* back */
  .scene {
    position: absolute; inset: 0;
    background:
      linear-gradient(90deg, var(--photo-wall) 0 32%, transparent 32%),
      linear-gradient(180deg, #e8d6b8 0%, var(--photo-warm) 55%, var(--photo-floor) 100%);
  }
  .badge {
    position: absolute;
    left: 26px; top: 22px;
    width: 197px; height: 49px;
    border-radius: 6px;
    background: rgba(255,255,255,.55);
  }
  .tagband {
    position: absolute;
    left: 0; right: 0; bottom: 0;
    height: 67px;
    background: var(--band-red);
    color: #fff;
    font-family: "Open Sans", sans-serif;
    text-align: center;
  }
  .tagband__title {
    margin: 6px 0 0;
    font-size: 21px;
    line-height: 26px;
  }
  .tagband__line {
    width: 480px; height: 1px; margin: 3px auto 4px;
    background: rgba(255,255,255,.35);
  }
  .tagband__note {
    margin: 0;
    font-size: 15px;
    font-style: italic;
  }
</style>
</head>
<body>
<main class="canvas">
  <section class="card card--front">
    <div class="brand brand--front">
      <span class="brand__square"></span>
      <span class="brand__name">Harbor9<br>Studio</span>
    </div>
    <div class="divider"></div>
    <div class="portrait" role="img" aria-label="Portrait photo of Tobias Merland in a circle"></div>
    <h1 class="person">Tobias Merland</h1>
    <ul class="contact">
      <li>
        <svg viewBox="0 0 24 24"><path d="M6.6 10.8a15.1 15.1 0 0 0 6.6 6.6l2.2-2.2a1 1 0 0 1 1-.25 11.4 11.4 0 0 0 3.6.57 1 1 0 0 1 1 1V20a1 1 0 0 1-1 1A17 17 0 0 1 3 4a1 1 0 0 1 1-1h3.5a1 1 0 0 1 1 1c0 1.25.2 2.45.57 3.57a1 1 0 0 1-.25 1z"/></svg>
        +49 160 55 82 907
      </li>
      <li>
        <svg viewBox="0 0 24 24"><path d="M2 5h20v14H2zm2 2v.5l8 5 8-5V7zm0 2.9V17h16V9.9l-8 5z"/></svg>
        tobias@harbor9studio.example
      </li>
      <li>
        <svg viewBox="0 0 24 24"><path d="M12 2a10 10 0 1 0 0 20 10 10 0 0 0 0-20zm-1 17.9A8 8 0 0 1 4.1 10L9 15v1a2 2 0 0 0 2 2zm6.9-2.5A2 2 0 0 0 16 16h-1v-3a1 1 0 0 0-1-1H8v-2h2a1 1 0 0 0 1-1V7h2a2 2 0 0 0 2-2v-.4a8 8 0 0 1 2.9 12.8z"/></svg>
        www.harbor9studio.example
      </li>
    </ul>
    <div class="rule-grey"></div>
    <div class="rule-red"></div>
  </section>

  <section class="card card--back">
    <div class="scene" role="img" aria-label="360° interior photo of a cosy restaurant dining room with wooden tables and red checked tablecloths"></div>
    <div class="badge" role="img" aria-label="Vornix Gold certification badge"></div>
    <div class="brand brand--back">
      <span class="brand__square"></span>
      <span class="brand__name">Harbor9<br>Studio</span>
    </div>
    <div class="tagband">
      <p class="tagband__title">360° vornix lanescope certified photographer</p>
      <div class="tagband__line"></div>
      <p class="tagband__note">send us a sms or pingwell and we call you back.</p>
    </div>
  </section>
</main>
</body>
</html>
```